Federal Government Proposal Development Consulting company needs a website designed and coded

I am looking for someone to design (using an existing logo, color palette, and text fonts) and code a wordpress-based website for a Proposal Development consulting company. I have full copy for all site pages and suggestions for images/ graphics and a few example design templates to go from.

One note, from a color perspective - I included a mockup of a business card to highlight a color scheme that I tend to like - if you look at the back of the business card, the blend of the grey, blue, with the neon green highlight as a separator really seems to pop. Just a thought as you are designing the page.

I would like to see 2-3 potential design layouts, and I will select one to move forward with. Then, I would like the site to be coded for WordPress (I can provide a login to my wordpress site). I would like 1 opportunity to review the coded site and make any final tweaks.

```html
<!DOCTYPE html>
<html lang="en">
<head>
<meta charset="utf-8">
<title>Quillmark Proposals Consulting LLC</title>
<link rel="stylesheet" href="https://fonts.googleapis.com/css2?family=Gabriela&family=Josefin+Sans:wght@300;400;600;700&display=swap">
<style>
:root{
  --blue:#0b3fc4;
  --navy:#0b0f4c;
  --ink:#222;
  --muted:#555;
  --soft:#eefcfd;
  --teal:#8fe6cf;
  --line:#e3e6ee;
  --white:#fff;
}
*{box-sizing:border-box;margin:0;padding:0}
html,body{width:1200px;height:4640px;overflow:hidden;background:var(--white)}
body{position:relative;font-family:"Josefin Sans",sans-serif;font-weight:300;color:var(--ink);font-size:13px}
b{font-weight:700}
.abs{position:absolute}
.serif{font-family:"Gabriela",serif;font-weight:400}
.btn{position:absolute;display:flex;align-items:center;justify-content:center;background:var(--blue);color:var(--white);border-radius:20px;font-size:12px;font-weight:400;letter-spacing:.5px}

/* header */
.site-header{position:absolute;left:0;top:0;width:1200px;height:97px;background:var(--white)}
.brand{position:absolute;left:140px;top:14px;display:flex;align-items:center;gap:8px}
.brand-name{font-family:"Gabriela",serif;font-size:26px;color:#666;line-height:1}
.brand-sub{font-family:"Gabriela",serif;font-size:11px;color:#888;margin-top:2px}
.brand-dot{width:20px;height:20px;border-radius:50%;background:var(--navy)}
.nav a{position:absolute;top:40px;font-size:12.5px;font-weight:400;color:#222;text-decoration:none}

/* hero */
.hero{position:absolute;left:0;top:97px;width:1200px;height:543px;background:linear-gradient(90deg,#2b2e33 0%,#4a4d52 35%,#9a9c9f 60%,#d6d3cc 100%)}
.hero-kicker{left:140px;top:296px;color:var(--teal);font-size:22px;font-weight:600}
.hero-title{left:140px;top:330px;color:var(--white);font-size:33px;line-height:50px}
.hero-sub{left:140px;top:436px;color:var(--white);font-size:15px;font-weight:400}

/* sections */
.section-title{position:absolute;width:1200px;text-align:center;font-family:"Gabriela",serif;font-weight:400;font-size:34px;color:var(--ink)}
.intro{left:198px;top:800px;width:804px;text-align:center;font-size:12.2px;line-height:19px;color:var(--muted)}
.intro p+p{margin-top:4px}
.card{position:absolute;top:1040px;width:283px;height:403px;background:var(--white);border-radius:10px;box-shadow:0 4px 18px rgba(0,0,0,.09);padding:34px 30px 0 32px}
.card-icon{position:absolute;top:-28px;left:30px;width:56px;height:56px;border-radius:50%;background:var(--blue);border:4px solid #d9e2fb;display:flex;align-items:center;justify-content:center}
.card h3{font-family:"Gabriela",serif;font-size:14px;font-weight:400;padding-bottom:10px;border-bottom:1px solid var(--line);margin-bottom:14px}
.card p{font-size:12px;line-height:18px;color:var(--muted);margin-bottom:12px}

.who-photo{left:142px;top:1703px;width:444px;height:502px;border-radius:0 110px 0 12px;background:linear-gradient(135deg,#d9dde2,#8c8f92 55%,#cfd1d3)}
.who-title{left:622px;top:1752px;font-size:34px}
.who-text{left:622px;top:1816px;width:436px;font-size:12.3px;line-height:23px;color:var(--muted)}

.svc{position:absolute;width:154px;height:125px;background:var(--white);box-shadow:0 2px 10px rgba(0,0,0,.08);display:flex;flex-direction:column;align-items:center;justify-content:center;text-align:center;font-size:13px;font-weight:400;line-height:15px;color:#333}
.svc svg{margin-bottom:10px}
.svc.active{background:var(--blue);color:var(--white);font-weight:700}

.sme-title{left:142px;top:3076px;font-size:34px}
.sme-list{left:142px;top:3152px;list-style:none}
.sme-list li{height:35.6px;display:flex;align-items:center;gap:14px;font-size:13.5px;font-weight:400;color:var(--navy)}
.sme-photo{left:614px;top:3068px;width:443px;height:504px;border-radius:60px 0 60px 0;background:linear-gradient(160deg,#6b5a4b,#2c2a28 40%,#e8e6e2 75%,#cfcbc4)}

.city{left:0;top:3640px;width:1200px;height:540px;background:linear-gradient(180deg,#2a3040,#6c6a68 60%,#9a948c)}
.contact-card{left:148px;top:3872px;width:904px;height:473px;background:var(--white);border-radius:14px;box-shadow:0 6px 24px rgba(0,0,0,.12)}
.contact-panel{left:170px;top:3890px;width:336px;height:435px;background:var(--blue);border-radius:12px;color:var(--white);padding:36px 38px}
.contact-panel h2{font-family:"Gabriela",serif;font-weight:400;font-size:32px;margin-bottom:20px}
.contact-panel .lead{font-size:12px;line-height:18px;margin-bottom:18px}
.info{display:flex;gap:14px;margin-bottom:18px;font-size:12px;line-height:18px}
.info b{font-weight:700;display:block}
.socials{display:flex;gap:9px;margin-top:4px}
.socials span{width:26px;height:26px;border:1.5px solid var(--white);border-radius:50%}
.git-title{left:536px;top:3938px;font-size:32px}
.field{position:absolute;width:234px;border-bottom:1px solid var(--line);padding-bottom:8px}
.field label{display:block;font-size:10px;color:#aaa;margin-bottom:6px}
.field span{font-size:12.5px;font-weight:400;color:#333}

.footer-brand{left:0;top:4438px;width:1200px;text-align:center}
.footer-nav{left:0;top:4552px;width:1200px;display:flex;justify-content:center;font-size:12px;font-weight:400;color:#333}
.footer-nav span{padding:0 20px;border-left:1px solid #999}
.footer-nav span:first-child{border-left:none}
.copy{left:142px;top:4614px;font-size:11.5px;font-weight:400;color:var(--navy)}
.legal{right:143px;top:4614px;font-size:11.5px;font-weight:400;color:var(--navy)}
</style>
</head>
<body>

<header class="site-header">
  <div class="brand">
    <div>
      <div class="brand-name">Quillmark</div>
      <div class="brand-sub">Consulting LLC</div>
    </div>
    <div class="brand-dot"></div>
  </div>
  <nav class="nav">
    <a style="left:481px;font-weight:700">Home</a>
    <a style="left:576px">Work with Us</a>
    <a style="left:712px">Work for Us</a>
    <a style="left:840px">About Us</a>
  </nav>
  <div class="btn" style="left:952px;top:29px;width:106px;height:38px;font-size:13px">Contact</div>
</header>

<section class="hero" role="img" aria-label="Photo of engineers in hard hats and a businessman reviewing plans"></section>
<div class="abs hero-kicker">Generate Successmodernize</div>
<h1 class="abs serif hero-title">Fuel Innovation in Proposal<br>Excellence with Quillmark!</h1>
<div class="abs hero-sub">Click here to explore our services.</div>
<div class="btn" style="left:140px;top:480px;width:198px;height:40px;font-weight:600">Explore Our Services</div>

<h2 class="section-title" style="top:732px">What We Do</h2>
<div class="abs intro">
  <p>Quillmark specializes in advancing an organization through a comprehensive suite of services designed to modernize the proposal development process. From innovative Capture Management strategies that pinpoint lucrative opportunities, meticulous Proposal Development services that transform concepts into effective narratives, and cutting-edge Generative AI techniques that create domain-aware content accelerating proposal draft development, we are your dedicated partner in securing success. With a unique fusion of technical expertise and exceptional writing capabilities, we surpass industry standards and set new benchmarks for excellence.</p>
  <p>Discover a dynamic approach to proposal consulting that goes beyond conventional boundaries—choose Quillmark for solutions that <b>Enhance</b> the quality of your work, <b>Elevate</b> your corporate advantage, and <b>Expand</b> your industry presence.</p>
</div>

<article class="card" style="left:142px">
  <div class="card-icon"><svg width="28" height="28" viewBox="0 0 28 28" fill="none" stroke="#fff" stroke-width="1.6"><rect x="7" y="7" width="14" height="14" rx="2"/><path d="M11 3v4M17 3v4M11 21v4M17 21v4M3 11h4M3 17h4M21 11h4M21 17h4"/></svg></div>
  <h3>Generative AI</h3>
  <p>Revolutionize your proposal writing process with our domain-aware Generative AI services. Using customer-installed tools, we leverage domain-aware artificial intelligence to generate innovative and tailored proposal content. This not only accelerates the proposal development timeline but also ensures content that is both dynamic and targeted.</p>
  <p>Stay ahead of the curve with proposals that not only meet industry standards but exceed expectations, thanks to the creative insights generated by our AI-driven approach.</p>
</article>
<article class="card" style="left:457px">
  <div class="card-icon"><svg width="28" height="28" viewBox="0 0 28 28" fill="none" stroke="#fff" stroke-width="1.6"><circle cx="12" cy="12" r="7"/><path d="M17 17l7 7"/><path d="M9 12h6M12 9v6"/></svg></div>
  <h3>Capture Management</h3>
  <p>Elevate your business development strategy with our Capture Management services. From opportunity identification to strategic planning, our experts will guide you through a meticulous process, ensuring the pursuit of the right contracts to position your organization for success.</p>
  <p>Trust us to analyze the market, mitigate risks, and develop strategies that maximize the ability to secure lucrative opportunities.</p>
</article>
<article class="card" style="left:772px">
  <div class="card-icon"><svg width="28" height="28" viewBox="0 0 28 28" fill="none" stroke="#fff" stroke-width="1.6"><rect x="7" y="4" width="14" height="20" rx="1.5"/><path d="M10 9h8M10 13h8M10 17h5"/></svg></div>
  <h3>Proposal Development</h3>
  <p>Transform your vision into winning proposals with our Proposal Development services. We specialize in persuasive narratives, clear technical solutions, and strategic pricing models. From meticulous compliance reviews to captivating executive summaries, we ensure every aspect of a proposal is polished and aligned with your objectives.</p>
  <p>Turn your ideas into persuasive documents that leave a lasting impression on clients to set you apart from the competition.</p>
</article>

<svg class="abs" style="left:0;top:1520px" width="1200" height="860" viewBox="0 0 1200 860" aria-hidden="true">
  <path d="M0 60 C200 20 350 40 500 60 C700 80 900 50 1200 40 L1200 760 C1000 720 800 790 600 800 C400 810 200 760 0 780 Z" fill="#eefcfd"/>
  <path d="M0 80 C120 30 300 35 500 60 C300 45 150 55 0 100 Z" fill="#0b0f4c"/>
  <path d="M850 770 C1000 760 1120 780 1200 820 L1200 850 C1110 800 1000 770 850 770 Z" fill="#0b0f4c"/>
</svg>

<div class="abs who-photo" role="img" aria-label="Photo of two businessmen talking at a table with a laptop"></div>
<h2 class="abs serif who-title">Who We Are</h2>
<div class="abs who-text">
  <p>It is a long established fact that a reader will be distracted by the readable content of a page when looking at its layout. The point of using Lorem Ipsum is that it has a more-or-less normal distribution of letters, as opposed to using 'Content here, content here', making it look like readable English. Many are desktop publishing packages and web page editors now use Lorem Ipsum as their default model text, and a search for 'lorem ipsum' will uncover many web sites still in their infancy.</p>
  <p>There are many variations of passages of Lorem Ipsum available, but the majority have suffered alteration in some form, by injected humour, or other randomised words which don't look even slightly believable.</p>
</div>
<div class="btn" style="left:622px;top:2120px;width:142px;height:34px;font-size:11px">ABOUT US</div>

<h2 class="section-title" style="top:2415px">Our Services</h2>
<div class="svc active" style="left:186px;top:2485px"><svg width="40" height="40" viewBox="0 0 40 40" fill="none" stroke="#fff" stroke-width="1.6"><rect x="11" y="11" width="18" height="18" rx="2"/><path d="M15 5v6M20 5v6M25 5v6M15 29v6M20 29v6M25 29v6M5 15h6M5 20h6M5 25h6M29 15h6M29 20h6M29 25h6"/></svg>Generative<br>AI</div>
<div class="svc" style="left:354px;top:2485px"><svg width="40" height="40" viewBox="0 0 40 40" fill="none" stroke="#333" stroke-width="1.5"><circle cx="22" cy="14" r="6"/><path d="M19 20v4h6v-4M22 4v3M14 8l2 2M30 8l-2 2M6 32h10l8-4h8"/></svg>Technical<br>Solutioning</div>
<div class="svc" style="left:522px;top:2485px"><svg width="40" height="40" viewBox="0 0 40 40" fill="none" stroke="#333" stroke-width="1.5"><path d="M12 34v-8c-4-3-5-8-3-13 3-6 11-8 17-4 5 4 5 10 3 13l3 5h-4v5h-6v2"/><circle cx="20" cy="17" r="4"/></svg>Competitive<br>Intelligence</div>
<div class="svc" style="left:690px;top:2485px"><svg width="40" height="40" viewBox="0 0 40 40" fill="none" stroke="#333" stroke-width="1.5"><circle cx="17" cy="14" r="7"/><path d="M5 34c0-8 5-12 12-12"/><circle cx="27" cy="28" r="6"/><path d="M31 32l4 4"/></svg>Capture<br>Management</div>
<div class="svc" style="left:858px;top:2485px"><svg width="40" height="40" viewBox="0 0 40 40" fill="none" stroke="#333" stroke-width="1.5"><rect x="10" y="5" width="20" height="30" rx="1.5"/><path d="M14 12h12M14 18h12M14 24h8"/></svg>Proposal<br>Management</div>

<div class="svc" style="left:186px;top:2625px"><svg width="40" height="40" viewBox="0 0 40 40" fill="none" stroke="#333" stroke-width="1.5"><rect x="11" y="4" width="18" height="18" rx="1.5"/><path d="M15 10h10M15 15h10M10 30l2-4 2 4M19 32l2-4 2 4M28 30l2-4 2 4"/></svg>Compliance<br>Reviews</div>
<div class="svc" style="left:354px;top:2625px"><svg width="40" height="40" viewBox="0 0 40 40" fill="none" stroke="#333" stroke-width="1.5"><circle cx="16" cy="16" r="9"/><rect x="20" y="20" width="13" height="14" rx="1"/><path d="M23 25h7M23 29h7"/></svg>Executive<br>Summaries</div>
<div class="svc" style="left:522px;top:2625px"><svg width="40" height="40" viewBox="0 0 40 40" fill="none" stroke="#333" stroke-width="1.5"><path d="M8 16h6l8-7v22l-8-7H8z"/><path d="M27 14c3 3 3 9 0 12M31 10c5 5 5 15 0 20"/></svg>Volume<br>Lead</div>
<div class="svc" style="left:690px;top:2625px"><svg width="40" height="40" viewBox="0 0 40 40" fill="none" stroke="#333" stroke-width="1.5"><circle cx="20" cy="9" r="4"/><path d="M14 35V20c0-4 12-4 12 0v15M26 22l5-10"/></svg>Technical<br>Writer</div>
<div class="svc" style="left:858px;top:2625px"><svg width="40" height="40" viewBox="0 0 40 40" fill="none" stroke="#333" stroke-width="1.5"><rect x="6" y="8" width="28" height="24" rx="1.5"/><path d="M20 8v24M10 14h6M10 19h6M10 24h6M24 14h6M24 19h6M24 24h6"/></svg>Book<br>Boss</div>

<div class="svc" style="left:186px;top:2775px"><svg width="40" height="40" viewBox="0 0 40 40" fill="none" stroke="#333" stroke-width="1.5"><rect x="7" y="5" width="20" height="28" rx="1.5"/><path d="M11 12h12M11 17h12M11 22h7M34 10L22 30l-2 4 4-2 12-20z"/></svg>Resume<br>Writer</div>
<div class="svc" style="left:354px;top:2775px"><svg width="40" height="40" viewBox="0 0 40 40" fill="none" stroke="#333" stroke-width="1.5"><rect x="5" y="7" width="30" height="20" rx="1.5"/><path d="M15 34h10M20 27v7"/></svg>Desktop<br>Publishing</div>
<div class="svc" style="left:522px;top:2775px"><svg width="40" height="40" viewBox="0 0 40 40" fill="none" stroke="#333" stroke-width="1.5"><rect x="12" y="4" width="20" height="28" rx="1.5"/><path d="M16 10h12M16 15h12M16 20h12M6 36h18M8 28h6v8"/></svg>Proposal<br>Production</div>
<div class="svc" style="left:690px;top:2775px"><svg width="40" height="40" viewBox="0 0 40 40" fill="none" stroke="#333" stroke-width="1.5"><path d="M10 4h14l6 6v26H10z"/><path d="M24 4v6h6M14 18h12M14 23h12M14 28h12"/></svg>Templates &amp;<br>Processes</div>
<div class="svc" style="left:858px;top:2775px"><svg width="40" height="40" viewBox="0 0 40 40" fill="none" stroke="#333" stroke-width="1.5"><rect x="9" y="6" width="20" height="28" rx="1.5"/><path d="M13 13h6M13 19h6M13 25h6M22 12l2 2 3-3M22 18l2 2 3-3M34 8L26 24"/></svg>Market<br>Survey</div>

<div class="btn" style="left:529px;top:2940px;width:142px;height:34px;font-size:11px">READ MORE</div>

<h2 class="abs serif sme-title">Subject Matter Expertise</h2>
<ul class="abs sme-list">
  <li><svg width="17" height="17" viewBox="0 0 17 17" fill="none" stroke="#0b3fc4" stroke-width="1.3"><circle cx="8.5" cy="8.5" r="7.5"/><path d="M5 8.5l2.5 2.5 4.5-5"/></svg>Generative AI</li>
  <li><svg width="17" height="17" viewBox="0 0 17 17" fill="none" stroke="#0b3fc4" stroke-width="1.3"><circle cx="8.5" cy="8.5" r="7.5"/><path d="M5 8.5l2.5 2.5 4.5-5"/></svg>Software/ Hardware Engineering</li>
  <li><svg width="17" height="17" viewBox="0 0 17 17" fill="none" stroke="#0b3fc4" stroke-width="1.3"><circle cx="8.5" cy="8.5" r="7.5"/><path d="M5 8.5l2.5 2.5 4.5-5"/></svg>Systems Engineering</li>
  <li><svg width="17" height="17" viewBox="0 0 17 17" fill="none" stroke="#0b3fc4" stroke-width="1.3"><circle cx="8.5" cy="8.5" r="7.5"/><path d="M5 8.5l2.5 2.5 4.5-5"/></svg>High-Performance Computing (HPC)</li>
  <li><svg width="17" height="17" viewBox="0 0 17 17" fill="none" stroke="#0b3fc4" stroke-width="1.3"><circle cx="8.5" cy="8.5" r="7.5"/><path d="M5 8.5l2.5 2.5 4.5-5"/></svg>Secure Supply Chain (ISO 28000 &amp; ISO 20243-1)</li>
  <li><svg width="17" height="17" viewBox="0 0 17 17" fill="none" stroke="#0b3fc4" stroke-width="1.3"><circle cx="8.5" cy="8.5" r="7.5"/><path d="M5 8.5l2.5 2.5 4.5-5"/></svg>Logistics, Warehousing</li>
  <li><svg width="17" height="17" viewBox="0 0 17 17" fill="none" stroke="#0b3fc4" stroke-width="1.3"><circle cx="8.5" cy="8.5" r="7.5"/><path d="M5 8.5l2.5 2.5 4.5-5"/></svg>Information Technology Support</li>
  <li><svg width="17" height="17" viewBox="0 0 17 17" fill="none" stroke="#0b3fc4" stroke-width="1.3"><circle cx="8.5" cy="8.5" r="7.5"/><path d="M5 8.5l2.5 2.5 4.5-5"/></svg>Cybersecurity</li>
  <li><svg width="17" height="17" viewBox="0 0 17 17" fill="none" stroke="#0b3fc4" stroke-width="1.3"><circle cx="8.5" cy="8.5" r="7.5"/><path d="M5 8.5l2.5 2.5 4.5-5"/></svg>Data Analysis</li>
  <li><svg width="17" height="17" viewBox="0 0 17 17" fill="none" stroke="#0b3fc4" stroke-width="1.3"><circle cx="8.5" cy="8.5" r="7.5"/><path d="M5 8.5l2.5 2.5 4.5-5"/></svg>Systems Integration</li>
  <li><svg width="17" height="17" viewBox="0 0 17 17" fill="none" stroke="#0b3fc4" stroke-width="1.3"><circle cx="8.5" cy="8.5" r="7.5"/><path d="M5 8.5l2.5 2.5 4.5-5"/></svg>Program Management</li>
  <li><svg width="17" height="17" viewBox="0 0 17 17" fill="none" stroke="#0b3fc4" stroke-width="1.3"><circle cx="8.5" cy="8.5" r="7.5"/><path d="M5 8.5l2.5 2.5 4.5-5"/></svg>Systems Development &amp; Testing</li>
</ul>
<div class="abs sme-photo" role="img" aria-label="Photo of a laptop showing a bar chart beside a coffee cup"></div>

<div class="abs city" role="img" aria-label="Photo of a city skyline with high-rise towers at dusk"></div>
<svg class="abs" style="left:0;top:3630px" width="1200" height="560" viewBox="0 0 1200 560" aria-hidden="true">
  <path d="M0 0 H1200 V40 C1000 80 850 20 650 40 C450 60 250 40 0 90 Z" fill="#fff"/>
  <path d="M0 90 C250 40 450 60 650 40 C850 20 1000 80 1200 40 V60 C1000 100 850 45 650 62 C450 80 250 70 0 120 Z" fill="#0b0f4c"/>
  <path d="M0 560 V470 C80 480 140 500 200 520 V560 Z M1200 560 V470 C1120 490 1080 520 1000 560 Z" fill="#fff"/>
</svg>

<div class="abs contact-card"></div>
<div class="abs contact-panel">
  <h2>Contact Us</h2>
  <p class="lead">Lorem Ipsum is simply dummy text of the printing and typesetting industry.</p>
  <div class="info"><svg width="16" height="18" viewBox="0 0 16 18" fill="#fff"><path d="M8 0a6 6 0 0 0-6 6c0 5 6 12 6 12s6-7 6-12a6 6 0 0 0-6-6zm0 8.5A2.5 2.5 0 1 1 8 3.5a2.5 2.5 0 0 1 0 5z"/></svg><div><b>Address</b>48 Harbor Lane, Suite 2,<br>Austin, Texas</div></div>
  <div class="info"><svg width="16" height="16" viewBox="0 0 16 16" fill="#fff"><path d="M3 1l3 3-2 2c1 2 3 4 5 5l2-2 3 3-2 3C7 15 1 9 0 3z"/></svg><div><b>Phone</b>123 456 7890</div></div>
  <div class="info"><svg width="16" height="14" viewBox="0 0 16 14" fill="none" stroke="#fff" stroke-width="1.4"><path d="M1 1h14v12H1zM1 2l7 6 7-6"/></svg><div><b>Email</b>inquiry@quillmarkco.com</div></div>
  <div class="socials"><span></span><span></span><span></span><span></span></div>
</div>
<h2 class="abs serif git-title">Get In Touch</h2>
<div class="field" style="left:536px;top:3998px"><label>Name</label><span>Lorem ipsum</span></div>
<div class="field" style="left:792px;top:3998px"><label>Email Address</label><span>info@quillmarkco.com</span></div>
<div class="field" style="left:536px;top:4082px"><label>Company Name</label><span>Lorem ipsum</span></div>
<div class="field" style="left:792px;top:4082px"><label>Phone Number</label><span>123-456-7890</span></div>
<div class="field" style="left:536px;top:4150px;width:490px;height:80px"><label>Message</label><span>Your Message is here</span></div>
<div class="btn" style="left:536px;top:4292px;width:142px;height:34px;font-size:11px">SEND NOW</div>

<div class="abs footer-brand">
  <div class="brand-name">Quillmark</div>
  <div class="brand-sub">Consulting LLC</div>
  <div style="width:20px;height:20px;border-radius:50%;background:var(--navy);margin:14px auto 0"></div>
</div>
<nav class="abs footer-nav"><span>HOME</span><span>WORK WITH US</span><span>WORK FOR US</span><span>ABOUT US</span><span>CONTACT US</span></nav>
<div class="abs copy">© 2024 Quillmark. All Rights Reserved.</div>
<div class="abs legal">Privacy Policy &nbsp;&nbsp;|&nbsp;&nbsp; Terms &amp; Conditions</div>

</body>
</html>
```